Hal's Remedies Business Card Design Project

I need a business card designed for my pharmacy Hal's Remedies. I would like just the logo on one side, maybe with black background and white lettering. The other side I would also like to include my logo which is attached. Also, please include my name and the following information:
Hal Norwick Owner/Pharm D.
Business address is 7163 N Birch Rd Sioux Falls, SD 57291.
Phone number is 605-318-6027 and fax # is 605-318-6031.
my email address is hal@halsremedies.example.
My website is www.halsremedies.example.
My business hours are Monday-Friday 8am-7 pm. Saturday 8am-12 pm. Sunday Closed.
I would like the design to include my logo colors, black, white, and neon green. Silver may be added as a highlight. Thanks.
Pharmacy
See above in product description

```html
<!DOCTYPE html>
<html lang="en">
<head>
<meta charset="utf-8">
<title>Hal's Remedies – Business Card</title>
<link rel="stylesheet" href="https://fonts.googleapis.com/css2?family=Open+Sans:wght@300;400;600&display=swap">
<style>
  :root {
    --backdrop: #e8e5e0;
    --card: #000000;
    --ink: #ffffff;
    --ink-soft: #e6e6e6;
    --neon: #9acd32;
    --pill-warm: #d9a07a;
    --pill-cool: #7fa9c9;
    --pill-pink: #d47a96;
  }
  * { box-sizing: border-box; margin: 0; padding: 0; }
  html, body {
    width: 1200px; height: 440px; overflow: hidden;
    background: var(--backdrop);
  }
  .canvas { position: relative; width: 1200px; height: 440px; }

  .card {
    position: absolute; top: 62px;
    width: 551px; height: 322px;
    background: var(--card);
    box-shadow: 0 2px 6px rgba(0,0,0,.25);
  }
  .card--front { left: 43px; }
  .card--back  { left: 607px; width: 550px; }

  /* Front */
  .brand-mark {
    position: absolute; left: 90px; top: 128px;
    width: 56px; height: 56px; border-radius: 50%;
    background: var(--neon);
  }
  .brand-divider {
    position: absolute; left: 171px; top: 113px;
    width: 2px; height: 88px; background: var(--ink);
  }
  .brand-name {
    position: absolute; left: 193px; top: 128px;
    font: 600 38px/56px "Open Sans", sans-serif;
    letter-spacing: -1px; color: var(--ink);
  }

  /* Back */
  .photo-strip {
    position: absolute; left: 0; top: 0;
    width: 100px; height: 322px;
    background: linear-gradient(170deg, var(--pill-warm) 0%, var(--pill-pink) 30%, var(--pill-cool) 55%, #e8d9a8 78%, var(--pill-warm) 100%);
  }
  .holder-name {
    position: absolute; left: 186px; top: 16px;
    font: 400 18px/24px "Open Sans", sans-serif;
    color: var(--ink); letter-spacing: .2px;
  }
  .contact-list { list-style: none; }
  .contact-item {
    position: absolute; left: 152px;
    display: flex; align-items: center;
    font: 300 15px/20px "Open Sans", sans-serif; color: var(--ink-soft);
  }
  .contact-icon {
    width: 20px; height: 20px; margin-right: 14px;
    fill: var(--ink); stroke: var(--ink);
  }
  .hours {
    position: absolute; left: 186px; top: 267px;
    font: 300 15px/19px "Open Sans", sans-serif; color: var(--ink-soft);
  }
</style>
</head>
<body>
<main class="canvas">

  <section class="card card--front" aria-label="Card front">
    <span class="brand-mark" aria-hidden="true"></span>
    <span class="brand-divider" aria-hidden="true"></span>
    <h1 class="brand-name">Hal's Remedies</h1>
  </section>

  <section class="card card--back" aria-label="Card back">
    <div class="photo-strip" role="img" aria-label="Photo of colourful pills and capsules"></div>
    <h2 class="holder-name">Hal Norwick Owner/Pharm D.</h2>
    <ul class="contact-list">
      <li class="contact-item" style="top:62px">
        <svg class="contact-icon" viewBox="0 0 20 20" aria-hidden="true"><path stroke="none" d="M10 1a6 6 0 0 0-6 6c0 4.5 6 12 6 12s6-7.5 6-12a6 6 0 0 0-6-6zm0 8.5a2.5 2.5 0 1 1 0-5 2.5 2.5 0 0 1 0 5z"/></svg>
        7163 N Birch Rd Sioux Falls, SD 57291.
      </li>
      <li class="contact-item" style="top:104px">
        <svg class="contact-icon" viewBox="0 0 20 20" aria-hidden="true"><path stroke="none" d="M5.5 2.5l3 3.5-1.8 2a10 10 0 0 0 5.3 5.3l2-1.8 3.5 3-1.6 2.6C10 17 3 10 2.9 4.1z"/></svg>
        605-318-6027
      </li>
      <li class="contact-item" style="top:144px">
        <svg class="contact-icon" viewBox="0 0 20 20" aria-hidden="true"><path stroke="none" d="M5 2h10v4H5zM2 7h16v8h-3v3H5v-3H2zm5 5v4h6v-4z"/></svg>
        605-318-6031.
      </li>
      <li class="contact-item" style="top:185px">
        <svg class="contact-icon" viewBox="0 0 20 20" aria-hidden="true"><g fill="none" stroke-width="1.4"><rect x="1.5" y="4" width="17" height="12"/><path d="M1.5 4l8.5 7 8.5-7M1.5 16l6-6M18.5 16l-6-6"/></g></svg>
        hal@halsremedies.example.
      </li>
      <li class="contact-item" style="top:226px">
        <svg class="contact-icon" viewBox="0 0 20 20" aria-hidden="true"><g fill="none" stroke-width="1.3"><circle cx="10" cy="10" r="8"/><ellipse cx="10" cy="10" rx="3.5" ry="8"/><path d="M2 10h16M3.5 6h13M3.5 14h13"/></g></svg>
        www.halsremedies.example.
      </li>
    </ul>
    <p class="hours">Monday-Friday 8am-7 pm. Saturday 8am-12 pm.<br>Sunday Closed</p>
  </section>

</main>
</body>
</html>
```